Business Card for my building company

I would like the card to make a statement, so as soon as you see the card you think "wow nice card' and then read the details on the card its self. Also i would like to be able to put in the detail for the MUST HAVES so please Crete a box that i can alter depending on who in my business needs the cards. Thank you

Target Market(s)

Any one looking to build a house/ townhouse or duplex

Industry/Entity Type

Home Builder

Contact Information for Business Card

I would like the card to have the logo on the card and the must haves

Font styles to use
Sans Serif

Requirements
Must have
• Name
• Phone Number
• Email Address
• Website
• Licence Number
• Abn

```html
<!DOCTYPE html>
<html lang="en">
<head>
<meta charset="utf-8">
<title>Ridgeline Builders – Business Card</title>
<link href="https://fonts.googleapis.com/css2?family=Montserrat:wght@400;500;700;800&display=swap" rel="stylesheet">
<style>
  :root {
    --backdrop: #2f2f30;
    --card: #f4f4f4;
    --card-edge: #e6e6e6;
    --ink: #1a1a1a;
    --gold: #c9a24e;
    --gold-deep: #a8822f;
    --detail-box: #dcdadb;
  }
  * { margin: 0; padding: 0; box-sizing: border-box; }
  html, body {
    width: 1200px; height: 1065px; overflow: hidden;
    background: var(--backdrop);
    font-family: "Montserrat", sans-serif;
  }
  .sheet {
    width: 1200px; height: 1065px;
    display: flex; flex-direction: column; align-items: center; justify-content: center;
    gap: 60px;
  }
  .card {
    position: relative;
    width: 760px; height: 440px;
    border-radius: 26px;
    background: radial-gradient(ellipse at 40% 45%, #ffffff 0%, var(--card) 60%, var(--card-edge) 100%);
    box-shadow: 0 10px 30px rgba(0,0,0,.35);
    overflow: hidden;
  }
  .brand {
    display: flex; align-items: center; gap: 14px;
    color: var(--gold);
    font-weight: 800;
    text-transform: uppercase;
    line-height: 1.05;
  }
  .brand-mark { background: var(--ink); flex: none; }
  .card-front .brand {
    position: absolute; left: 50%; top: 50%; transform: translate(-50%, -50%);
    font-size: 46px; gap: 20px;
  }
  .card-front .brand-mark { width: 62px; height: 62px; }

  .card-back .detail-box {
    position: absolute; left: 372px; top: 34px;
    width: 330px; height: 210px;
    background: var(--detail-box);
  }
  .card-back .brand {
    position: absolute; left: 56px; top: 196px;
    font-size: 26px;
  }
  .card-back .brand-mark { width: 38px; height: 38px; }
  .contact {
    position: absolute; left: 56px; top: 268px;
    list-style: none;
    font-size: 15px; color: var(--ink);
  }
  .contact li { display: flex; align-items: center; gap: 10px; height: 23px; }
  .contact .name {
    color: var(--gold); font-weight: 700; letter-spacing: 2px; font-size: 14px;
    margin-bottom: 4px;
  }
  .contact .icon { width: 14px; height: 14px; fill: var(--gold-deep); flex: none; }
  .contact .gold { color: var(--gold); padding-left: 24px; }
</style>
</head>
<body>
<main class="sheet">
  <section class="card card-front" aria-label="Card front">
    <div class="brand">
      <span class="brand-mark"></span>
      <span>Ridgeline<br>Builders</span>
    </div>
  </section>

  <section class="card card-back" aria-label="Card back">
    <div class="detail-box" role="img" aria-label="Editable box for staff details"></div>
    <div class="brand">
      <span class="brand-mark"></span>
      <span>Ridgeline<br>Builders</span>
    </div>
    <ul class="contact">
      <li class="name">YOUR NAME</li>
      <li>
        <svg class="icon" viewBox="0 0 16 16"><path d="M3.6 1.2l2.3 2.9c.3.4.3.9-.1 1.3L4.6 6.6c.9 2 2.6 3.8 4.8 4.8l1.2-1.2c.4-.4.9-.4 1.3-.1l2.9 2.3c.4.3.4.9 0 1.3l-1.3 1.3C11.8 16.6 0 7.9 1 2.5L2.3 1.2c.4-.4 1-.4 1.3 0z"/></svg>
        <span>123-456-789</span>
      </li>
      <li>
        <svg class="icon" viewBox="0 0 16 16"><path d="M1 3h14v10H1z"/><path d="M1 3l7 6 7-6" fill="none" stroke="#fff" stroke-width="1.4"/></svg>
        <span>admin@ridgelinebuilders.com</span>
      </li>
      <li>
        <svg class="icon" viewBox="0 0 16 16"><path d="M1 2h14v9H1zM2.4 3.4v6.2h11.2V3.4zM6 12h4v1.5h2V15H4v-1.5h2z"/></svg>
        <span>www.ridgelinebuilders.com</span>
      </li>
      <li class="gold">123-456-789</li>
      <li class="gold">ABN 123456789</li>
    </ul>
  </section>
</main>
</body>
</html>
```